Business Card Design

I am a GP with interest in Dermatology and Aesthetic Medicin, performing Botulinum Toxin Type A and Dermal Fillers treatmets in Cosmetic Dermatology clinic.

I am looking for a white colour, good quality white paper card may be of some special texture with black calligraphic writing but easy to read and not to wiggly- professional- looking.

Really appreciate your help.

Halyna

Cosmetic Dermatology Clinic

Dr Halyna Korbutiak, MBBS, MRCGP, DPD

Tel: 07841 615 092
halyna@medmailbox.org.uk

```html
<!DOCTYPE html>
<html lang="en">
<head>
<meta charset="utf-8">
<title>Business Card – Dr Halyna Korbutiak</title>
<link rel="stylesheet" href="https://fonts.googleapis.com/css2?family=Cormorant+Garamond:ital,wght@0,500;1,500&family=Cormorant+SC:wght@600&family=Arimo:wght@400&display=swap">
<style>
  :root {
    --backdrop: #2b2c2e;
    --paper: #ffffff;
    --ink: #111111;
    --accent: #5a9fd8;
    --accent-soft: #a9d2ea;
    --blue-deep: #1d4fa3;
    --blue-mid: #3b78c4;
    --blue-light: #6fa7dc;
    --strip: #3f6fb8;
    --contact: #ffffff;
  }
  * { margin: 0; padding: 0; box-sizing: border-box; }
  html, body { width: 1200px; height: 900px; overflow: hidden; }
  body {
    background: var(--backdrop);
    position: relative;
    font-family: "Arimo", Arial, sans-serif;
  }
  .card {
    position: absolute;
    left: 320px;
    width: 560px;
    height: 320px;
    overflow: hidden;
    box-shadow: 0 10px 30px rgba(0,0,0,0.45);
  }
  .card--front { top: 100px; background: var(--paper); }
  .card--back { top: 470px; }

  /* Front */
  .front__brand {
    position: absolute;
    left: 44px;
    top: 196px;
    display: flex;
    align-items: center;
    gap: 10px;
  }
  .brand__dot {
    width: 30px; height: 30px;
    border-radius: 50%;
    background: var(--accent-soft);
  }
  .brand__name {
    font-family: "Cormorant Garamond", Georgia, serif;
    font-weight: 500;
    font-size: 22px;
    color: var(--accent);
    letter-spacing: 2px;
  }
  .front__details {
    position: absolute;
    left: 230px;
    top: 72px;
  }
  .details__clinic {
    font-family: "Cormorant SC", Georgia, serif;
    font-weight: 600;
    font-size: 19px;
    color: var(--ink);
    letter-spacing: 1.5px;
  }
  .details__name {
    font-family: "Cormorant Garamond", Georgia, serif;
    font-style: italic;
    font-weight: 500;
    font-size: 28px;
    color: var(--accent);
    letter-spacing: 3px;
    margin-top: 2px;
  }
  .details__quals {
    font-family: "Arimo", Arial, sans-serif;
    font-size: 12px;
    color: var(--ink);
    letter-spacing: 5px;
    margin-top: 2px;
  }

  /* Back */
  .back__field {
    position: absolute; inset: 0;
    background:
      radial-gradient(ellipse at 30% 20%, rgba(160,205,240,0.55), transparent 55%),
      radial-gradient(ellipse at 75% 80%, rgba(120,180,230,0.35), transparent 60%),
      linear-gradient(160deg, var(--blue-light) 0%, var(--blue-mid) 45%, var(--blue-deep) 100%);
  }
  .back__strip {
    position: absolute;
    left: 0; top: 52px;
    width: 340px; height: 34px;
    background: var(--strip);
    opacity: 0.85;
  }
  .back__band {
    position: absolute;
    left: 0; top: 86px;
    width: 100%; height: 74px;
    background: var(--paper);
    display: flex;
    align-items: center;
    padding-left: 34px;
    gap: 14px;
  }
  .band__dot {
    width: 34px; height: 34px;
    border-radius: 50%;
    background: var(--accent-soft);
  }
  .band__name {
    font-family: "Cormorant Garamond", Georgia, serif;
    font-style: italic;
    font-weight: 500;
    font-size: 30px;
    color: var(--accent);
    letter-spacing: 5px;
  }
  .back__contact {
    position: absolute;
    right: 40px;
    bottom: 46px;
    color: var(--contact);
    font-size: 19px;
    letter-spacing: 1.5px;
    list-style: none;
  }
  .contact__item {
    display: flex;
    align-items: center;
    gap: 10px;
    line-height: 1.35;
  }
  .contact__icon { width: 20px; height: 16px; fill: var(--contact); }
</style>
</head>
<body>

  <section class="card card--front" aria-label="Business card front">
    <div class="front__details">
      <p class="details__clinic">Cosmetic Dermatology Clinic</p>
      <p class="details__name">Dr Halyna Korbutiak</p>
      <p class="details__quals">MBBS, MRCGP, DPD</p>
    </div>
    <div class="front__brand">
      <span class="brand__dot"></span>
      <span class="brand__name">Korbutiak</span>
    </div>
  </section>

  <section class="card card--back" aria-label="Business card back">
    <div class="back__field" role="img" aria-label="Soft blue background with flowing light curves"></div>
    <div class="back__strip"></div>
    <div class="back__band">
      <span class="band__dot"></span>
      <span class="band__name">Halyna Korbutiak</span>
    </div>
    <ul class="back__contact">
      <li class="contact__item">
        <svg class="contact__icon" viewBox="0 0 20 16" aria-hidden="true">
          <path d="M1 5 Q10 -1 19 5 L17 7 L14 6 L14 4 Q10 3 6 4 L6 6 L3 7 Z"/>
          <rect x="3" y="8" width="14" height="7" rx="1"/>
        </svg>
        <span>07841 615 092</span>
      </li>
      <li class="contact__item">
        <svg class="contact__icon" viewBox="0 0 20 16" aria-hidden="true">
          <rect x="1" y="2" width="18" height="12" rx="1"/>
          <path d="M1.5 2.5 L10 9 L18.5 2.5" fill="none" stroke="#2b5fae" stroke-width="1.4"/>
        </svg>
        <span>halyna@medmailbox.org.uk</span>
      </li>
    </ul>
  </section>

</body>
</html>
```